" Somos em 2 escritorios no Brasil. 1 em BH e outro em SP aonde eu fico. Eu acabei assumindo 100% da empresa e sou agora independente da Lumivar,BH porém continuamos parceiros e as duas empresas continuam a Se chamar Lùmivar`. Inclusive usamos os mesmo e.mail (as 2 empresas). Todavia no acordo de separação combinamos que eu sm SP mudarei um pouco o Logo "

```html
<!DOCTYPE html>
<html lang="pt-BR">
<head>
<meta charset="utf-8">
<title>Lumivar – Assinatura de e-mail</title>
<link rel="stylesheet" href="https://fonts.googleapis.com/css2?family=Roboto+Condensed:wght@400;700&display=swap">
<style>
  :root {
    --page-bg: #ececec;
    --card-white: #ffffff;
    --brand-blue: #3a5da6;
    --brand-red: #d2192b;
    --text-white: #ffffff;
    --brand-gray: #6b6d70;
  }
  * { margin: 0; padding: 0; box-sizing: border-box; }
  html, body {
    width: 1200px; height: 1200px; overflow: hidden;
    background: var(--page-bg);
    font-family: "Roboto Condensed", Arial, sans-serif;
  }
  .signature {
    position: absolute; left: 48px; top: 497px;
    width: 1104px; height: 278px;
    border-radius: 24px; overflow: hidden;
    box-shadow: 0 6px 18px rgba(0,0,0,.18);
  }
  .signature-shape { position: absolute; inset: 0; }
  .brand {
    position: absolute; left: 0; top: 0; width: 456px; height: 278px;
    display: flex; align-items: center; justify-content: center; gap: 16px;
  }
  .brand-dot { width: 34px; height: 34px; border-radius: 50%; background: var(--brand-blue); }
  .brand-name {
    font-size: 64px; font-weight: 400; letter-spacing: 2px;
    color: var(--brand-gray); line-height: 1;
  }
  .details { position: absolute; left: 552px; top: 0; color: var(--text-white); }
  .person-name {
    position: absolute; left: 0; top: 20px; white-space: nowrap;
    font-size: 40px; font-weight: 700; letter-spacing: .5px;
  }
  .person-role {
    position: absolute; left: 0; top: 66px; white-space: nowrap;
    font-size: 22px; font-weight: 400;
  }
  .contact-icon { position: absolute; left: 0; width: 32px; height: 32px; }
  .contact-line {
    position: absolute; left: 58px; white-space: nowrap;
    font-size: 20px; line-height: 24px; font-weight: 400;
  }
  .contact-line b { font-weight: 700; }
</style>
</head>
<body>
  <section class="signature">
    <svg class="signature-shape" viewBox="0 0 1104 278" width="1104" height="278">
      <rect width="1104" height="278" fill="var(--card-white)"/>
      <path d="M476 0 C462 70 452 170 452 278 L1104 278 L1104 0 Z" fill="var(--brand-red)"/>
      <path d="M488 0 C472 70 462 170 462 278 L1104 278 L1104 0 Z" fill="var(--brand-blue)"/>
    </svg>

    <div class="brand">
      <span class="brand-dot"></span>
      <span class="brand-name">LUMIVAR</span>
    </div>

    <div class="details">
      <p class="person-name">NOME COMPLETO</p>
      <p class="person-role">CARGO OU FUNÇÃO</p>

      <svg class="contact-icon" style="top:106px" viewBox="0 0 32 32" aria-label="Telefone">
        <circle cx="16" cy="16" r="16" fill="var(--brand-red)"/>
        <path d="M11 8 L14 8 L15 12 L13 14 C14 17 15 18 18 19 L20 17 L24 18 L24 21 C24 23 22 24 20 24 C14 23 9 18 8 12 C8 10 9 8 11 8 Z" fill="var(--text-white)"/>
      </svg>
      <p class="contact-line" style="top:100px">00 0000.00000</p>
      <p class="contact-line" style="top:122px">00 0000.00000</p>

      <svg class="contact-icon" style="top:164px" viewBox="0 0 32 32" aria-label="Site e e-mail">
        <circle cx="16" cy="16" r="16" fill="var(--brand-red)"/>
        <g fill="none" stroke="var(--text-white)" stroke-width="2">
          <circle cx="16" cy="16" r="8"/>
          <ellipse cx="16" cy="16" rx="3.5" ry="8"/>
          <path d="M8 16 H24"/>
        </g>
      </svg>
      <p class="contact-line" style="top:160px">LUMIVARFRETES.COM.BR</p>
      <p class="contact-line" style="top:182px">CONTATO@LUMIVARFRETES.COM.BR</p>

      <svg class="contact-icon" style="top:216px" viewBox="0 0 32 32" aria-label="Endereço">
        <circle cx="16" cy="16" r="16" fill="var(--brand-red)"/>
        <path d="M16 7 C12 7 10 10 10 13 C10 17 16 25 16 25 C16 25 22 17 22 13 C22 10 20 7 16 7 Z" fill="var(--text-white)"/>
        <circle cx="16" cy="13" r="2.5" fill="var(--brand-red)"/>
      </svg>
      <p class="contact-line" style="top:210px">NOME DA RUA, 000 - BAIRRO</p>
      <p class="contact-line" style="top:232px"><b>CIDADE</b> - ESTADO - <b>CEP</b> E PAIS</p>
    </div>
  </section>
</body>
</html>
```